Zielgruppe
Wir sind ein Fachpflegedienst für außerklinische Intensivpflege. Unsere Zielgruppe sind Patienten, Angehörige, Krankenkassen und Kliniken
Aufgabenstellung
Wir benötigen ein ansprechendes Briefpapier. Das Design soll zu unserer Webseite und unserer Broschüre passen. Die Webseite ist www.korvalin37.de und die Broschüre ist im Anhang. Wichtig ist, dass die Badges auf dem Briefpapier zu sehen sind.

```html
<!DOCTYPE html>
<html lang="de">
<head>
<meta charset="utf-8">
<title>Korvalin37 Briefpapier</title>
<link href="https://fonts.googleapis.com/css2?family=Roboto:wght@400;500;700&display=swap" rel="stylesheet">
<style>
  :root {
    --brand-blue: #1f4f93;
    --brand-red: #e3101b;
    --tint-blue: #eaf2fb;
    --ink: #1b1b1b;
    --muted: #444;
    --backdrop: #f1f1f1;
    --paper: #ffffff;
  }
  * { margin: 0; padding: 0; box-sizing: border-box; }
  html, body { width: 1200px; height: 1200px; overflow: hidden; background: var(--backdrop); font-family: "Roboto", Arial, sans-serif; }
  .letter { position: absolute; left: 195px; top: 27px; width: 810px; height: 1146px; background: var(--paper); box-shadow: 2px 3px 6px rgba(0,0,0,.25); overflow: hidden; color: var(--ink); }
  .header-shapes, .footer-shapes { position: absolute; left: 0; width: 810px; }
  .header-shapes { top: 0; height: 100px; }
  .footer-shapes { bottom: 0; height: 100px; }
  .tagline { position: absolute; left: 41px; top: 36px; font-size: 18px; font-weight: 500; color: var(--brand-blue); letter-spacing: .3px; }
  .brand { position: absolute; left: 575px; top: 118px; display: flex; align-items: center; gap: 9px; }
  .brand-mark { width: 16px; height: 16px; background: var(--brand-blue); }
  .brand-name { font-size: 24px; font-weight: 400; color: var(--brand-blue); line-height: 1; }
  .contact { position: absolute; left: 575px; top: 180px; font-size: 10px; line-height: 14.4px; color: var(--ink); }
  .contact p + p { margin-top: 14px; }
  .contact .web { color: var(--brand-red); font-weight: 500; }
  .sender-line { position: absolute; left: 78px; top: 183px; font-size: 6.4px; color: var(--muted); border-bottom: .6px solid var(--muted); padding-bottom: 1px; }
  .margin-mark { position: absolute; left: 0; width: 34px; height: 1.2px; background: var(--brand-red); }
  .content { position: absolute; left: 78px; top: 396px; width: 652px; }
  .reference { font-size: 19.5px; font-weight: 500; letter-spacing: .2px; margin-bottom: 27px; }
  .salutation, .body p, .closing { font-size: 13.1px; line-height: 19px; }
  .salutation { margin-bottom: 19px; }
  .body p { text-align: justify; margin-bottom: 19px; }
  .closing { margin-top: 37px; }
  .signature { width: 148px; height: 86px; margin-top: 6px; background: linear-gradient(90deg, #f4f4f4, #e9e9e9); border-radius: 4px; }
  .badges { position: absolute; left: 56px; top: 1058px; display: flex; align-items: center; gap: 16px; }
  .badge { background: #d7dde6; }
  .badge.round { width: 56px; height: 56px; border-radius: 50%; }
  .badge.square { width: 36px; height: 48px; background: #2d4d8c; }
  .badge.wide { width: 72px; height: 40px; border-radius: 6px; background: #eef1f5; border: 1px solid #d6dbe3; }
  .badge.seal { width: 54px; height: 54px; border-radius: 50%; background: #e6eef9; border: 2px solid #6d9ad8; }
  .legal { position: absolute; top: 1078px; font-size: 9.2px; line-height: 14.4px; color: var(--brand-blue); letter-spacing: .2px; }
  .legal.bank { left: 391px; }
  .legal.register { left: 587px; }
</style>
</head>
<body>
  <article class="letter">
    <svg class="header-shapes" viewBox="0 0 810 100" aria-hidden="true">
      <polygon points="0,0 471,0 431,92 0,92" fill="var(--tint-blue)"/>
      <polygon points="472,0 810,0 810,19 466,19" fill="var(--brand-blue)"/>
    </svg>
    <div class="tagline">MIT FACHKOMPETENZ UND FÜRSORGE</div>

    <div class="brand">
      <span class="brand-mark"></span>
      <span class="brand-name">Korvalin37</span>
    </div>

    <div class="contact">
      <p>Korvalin37 GmbH<br>Kastanienallee 14<br>71034 Böblingen</p>
      <p>Tel: (07031) – 482 930 0<br>Fax: (07031) – 482 930 2</p>
      <p class="web">info@korvalin37.de<br>www.korvalin37.de</p>
    </div>

    <div class="sender-line">Korvalin37 GmbH · Kastanienallee 14 · 71034 Böblingen</div>

    <span class="margin-mark" style="top:406px"></span>
    <span class="margin-mark" style="top:573px"></span>

    <main class="content">
      <h1 class="reference">Geschäfts-Nr. FE1221205-L/K08</h1>
      <p class="salutation">Sehr geehrte Frau Musterfrau,</p>
      <div class="body">
        <p>Lorem ipsum dolor sit amet, consectetuer adipiscing elit. Aenean commodo ligula eget dolor. Aenean massa. Cum sociis natoque penatibus et magnis dis parturient montes, nascetur ridiculus mus. Donec quam felis, ultricies nec, pellentesque eu, pretium quis, sem.</p>
        <p>Nulla consequat massa quis enim. Donec pede justo, fringilla vel, aliquet nec, vulputate eget, arcu. In enim justo, rhoncus ut, imperdiet a, venenatis vitae, justo. Nullam dictum felis eu pede mollis pretium. Integer tincidunt.</p>
        <p>Cras dapibus. Vivamus elementum semper nisi. Aenean vulputate eleifend tellus. Aenean leo ligula, porttitor eu, consequat vitae, eleifend ac, enim. Aliquam lorem ante, dapibus in, viverra quis, feugiat a, tellus. Phasellus viverra nulla ut metus varius laoreet. Quisque rutrum. Aenean imperdiet. Etiam ultricies nisi vel augue. Curabitur ullamcorper ultricies nisi. Nam eget dui.</p>
      </div>
      <p class="closing">Mit freundlichen Grüßen</p>
      <div class="signature" role="img" aria-label="Handschriftliche Unterschrift"></div>
    </main>

    <svg class="footer-shapes" viewBox="0 0 810 100" aria-hidden="true">
      <polygon points="379,6 810,6 810,100 342,100" fill="var(--tint-blue)"/>
      <polygon points="0,80 338,80 330,100 0,100" fill="var(--brand-red)"/>
    </svg>

    <div class="badges">
      <div class="badge round" role="img" aria-label="Empfehlungssiegel"></div>
      <div class="badge square" role="img" aria-label="Arbeitgeber-Auszeichnung"></div>
      <div class="badge wide" role="img" aria-label="Bewertungsabzeichen"></div>
      <div class="badge seal" role="img" aria-label="Zertifizierungssiegel"></div>
    </div>

    <div class="legal bank">
      Bankverbindung:<br>
      Südwest Gesundheitsbank<br>
      IBAN: DE41 6005 0101 0078 3310 42<br>
      BIC: SWGBDESSXXX
    </div>
    <div class="legal register">
      Institutionskennzeichen: 470923186<br>
      Registergericht: Stuttgart<br>
      Registernummer: HRB 761 294<br>
      Umsatzsteuer-ID: DE318562047
    </div>
  </article>
</body>
</html>
```